New Business Card Design Project

We are looking for a talented individual to create a truly awesome/unique business card design for us. We are looking for a someone to design something that will really stand out from the crowd - we don't mind what ideas you come up with (ie embossed/flat/matte/shine etc etc) just wow us with your creativity.
Updates

Target Market(s)

Video Games Industry Professionals (all levels of seniority from QA Testers through to CEOs)

Contact Information for Business Card

Company logo (see upload)
Company name: Northbay Play Careers Ltd
Employee Name: Darren Elsby
Job title: CEO
Website: www.nbpc2go.example
Office +44 1632 960418
Mobile: +44 7700 900276
Email: darren@nbpc2go.example

Colors

Designer to choose colors to be used in the design.

Requirements
Must have
• The business card design MUST contain all the information listed in the BUSINESS CARD DETAILS box.
• You will see the colours that are relevant to us (ie company logo) in the uploaded imagery - however you do not have to use all these colours when designing the business card itself
• MUST BE DOUBLE SIDED

```html
<!DOCTYPE html>
<html lang="en">
<head>
<meta charset="utf-8">
<title>Northbay Play Careers – Business Card</title>
<link rel="stylesheet" href="https://fonts.googleapis.com/css2?family=Lato:wght@400;700&display=swap">
<style>
  :root {
    --navy: #2f3a64;
    --orange: #ef7a1a;
    --paper: #ffffff;
    --ink: #1f2448;
    --ghost: #eeeff2;
    --backdrop: #c9d3d6;
  }
  * { margin: 0; padding: 0; box-sizing: border-box; }
  html, body { width: 1200px; height: 960px; overflow: hidden; }
  body {
    background: var(--backdrop);
    font-family: "Lato", sans-serif;
    position: relative;
  }
  .card {
    position: absolute;
    left: 300px;
    width: 600px;
    height: 343px;
    border-radius: 4px;
    overflow: hidden;
    box-shadow: 0 8px 24px rgba(20, 30, 50, 0.25);
  }
  .card--front { top: 100px; background: var(--paper); }
  .card--back { top: 517px; background: var(--navy); }

  .brand { position: absolute; display: flex; align-items: center; gap: 14px; }
  .brand__dot { width: 44px; height: 44px; border-radius: 50%; flex: none; }
  .brand__name { font-weight: 700; font-size: 26px; line-height: 1.15; }

  .card--front .brand { left: 40px; top: 46px; }
  .card--front .brand__dot { background: var(--orange); }
  .card--front .brand__name { color: var(--navy); }

  .ghost-mark {
    position: absolute; right: -40px; top: 20px;
    width: 260px; height: 260px; border-radius: 50%;
    background: var(--ghost);
  }

  .person { position: absolute; left: 40px; top: 176px; color: var(--ink); }
  .person__name { font-size: 25px; font-weight: 400; }
  .person__title { font-size: 15px; margin-top: 8px; }

  .contacts { position: absolute; left: 40px; top: 240px; list-style: none; color: var(--ink); font-size: 14px; }
  .contacts li { display: flex; align-items: center; gap: 14px; height: 20px; }
  .contacts svg { width: 12px; height: 12px; fill: var(--ink); }

  .band {
    position: absolute; left: 0; right: 0; bottom: 0; height: 26px;
    background: var(--navy);
  }
  .band__url {
    position: absolute; right: 30px; bottom: 32px;
    font-size: 12px; color: var(--navy); letter-spacing: 0.5px;
  }

  .card--back .brand { left: 50%; top: 118px; transform: translateX(-50%); white-space: nowrap; }
  .card--back .brand__dot { background: var(--orange); }
  .card--back .brand__name { color: var(--paper); font-size: 30px; }
  .back-url {
    position: absolute; left: 0; right: 0; top: 232px; text-align: center;
    color: var(--paper); font-size: 13px; letter-spacing: 1px;
  }
</style>
</head>
<body>
  <section class="card card--front">
    <div class="ghost-mark" aria-hidden="true"></div>
    <div class="brand">
      <span class="brand__dot"></span>
      <span class="brand__name">Northbay Play Careers</span>
    </div>
    <div class="person">
      <p class="person__name">Darren Elsby</p>
      <p class="person__title">CEO</p>
    </div>
    <ul class="contacts">
      <li><svg viewBox="0 0 12 12"><path d="M2.5 0.5l2 2-1 1.5c.6 1.4 1.6 2.4 3 3l1.5-1 2 2-1.3 1.8C5.5 10.5 1.5 6.5 0.7 1.8z"/></svg>+44 1632 960418</li>
      <li><svg viewBox="0 0 12 12"><path d="M3 0h6v12H3zM4 1.5v7h4v-7z"/></svg>+44 7700 900276</li>
      <li><svg viewBox="0 0 12 12"><path d="M0 2h12v8H0zM1 3l5 3.5L11 3z"/></svg>darren@nbpc2go.example</li>
    </ul>
    <span class="band__url">www.nbpc2go.example</span>
    <div class="band"></div>
  </section>

  <section class="card card--back">
    <div class="brand">
      <span class="brand__dot"></span>
      <span class="brand__name">Northbay Play Careers</span>
    </div>
    <p class="back-url">www.nbpc2go.example</p>
  </section>
</body>
</html>
```